Love pets? Create a veterinary business card that aligns with our new revamped website.

Greetings! We are a five-doctor veterinary hospital that seeks your expertise in designing a new business card that harmonizes with our recently revitalized website: www.tqrn.net. The card should feature our logo, the five doctors, operating hours, contact information, and communicate our purpose and personality.

Contact Information for Business Card

TBA

```html
<!DOCTYPE html>
<html lang="en">
<head>
<meta charset="utf-8">
<title>Maple Hollow Veterinary Hospital – Business Card</title>
<link rel="stylesheet" href="https://fonts.googleapis.com/css2?family=Lato:wght@400;700;900&display=swap">
<style>
  :root {
    --bg: #e9e9e9;
    --card: #fbfbfa;
    --green: #3f8f3a;
    --brown: #7b5a2b;
    --slate: #8aa3ad;
    --orange: #d99a35;
    --ink: #4a4a4a;
  }
  * { box-sizing: border-box; margin: 0; padding: 0; }
  html, body { width: 1200px; height: 930px; overflow: hidden; }
  body {
    background: var(--bg);
    font-family: "Lato", sans-serif;
    position: relative;
  }
  .card {
    position: absolute;
    left: 320px;
    width: 560px;
    height: 320px;
    background: var(--card);
    border-radius: 26px;
    box-shadow: 0 6px 18px rgba(0,0,0,0.12);
    overflow: hidden;
  }
  .card--front { top: 100px; }
  .card--back { top: 500px; }

  /* Front */
  .brand {
    position: absolute;
    left: 0; right: 0; top: 118px;
    display: flex;
    align-items: center;
    justify-content: center;
    gap: 16px;
  }
  .brand__mark {
    width: 46px; height: 46px;
    border-radius: 50%;
    background: var(--green);
  }
  .brand__name {
    font-weight: 700;
    font-size: 27px;
    color: var(--green);
    letter-spacing: 0.5px;
    line-height: 1.15;
  }
  .color-bar {
    position: absolute;
    left: 0; right: 0; bottom: 0;
    height: 12px;
    display: flex;
    gap: 4px;
  }
  .color-bar span { flex: 1; }
  .color-bar .green { background: var(--green); }
  .color-bar .brown { background: var(--brown); }
  .color-bar .slate { background: var(--slate); }
  .color-bar .orange { background: var(--orange); }

  /* Back */
  .mini-brand {
    position: absolute;
    right: 34px; top: 28px;
    display: flex;
    align-items: center;
    gap: 8px;
  }
  .mini-brand__mark {
    width: 22px; height: 22px; border-radius: 50%;
    background: var(--green);
  }
  .mini-brand__name {
    font-weight: 700; font-size: 12px; color: var(--green);
  }
  .doctors {
    position: absolute;
    left: 40px; top: 104px;
    width: 210px;
    text-align: right;
  }
  .doctors li {
    list-style: none;
    font-weight: 900;
    font-size: 17px;
    line-height: 21px;
    color: var(--green);
    text-transform: uppercase;
  }
  .doctors .credential {
    font-weight: 400;
    font-size: 15px;
    color: var(--brown);
    margin-top: 2px;
  }
  .divider {
    position: absolute;
    left: 270px; top: 96px;
    width: 1.5px; height: 132px;
    background: var(--orange);
  }
  .contact {
    position: absolute;
    left: 290px; top: 96px;
  }
  .contact li {
    list-style: none;
    display: flex;
    align-items: center;
    gap: 10px;
    font-size: 13.5px;
    line-height: 21px;
    color: var(--ink);
  }
  .contact li.cont { padding-left: 22px; }
  .contact svg { width: 12px; height: 12px; flex: none; fill: var(--brown); }
  .hours {
    position: absolute;
    left: 40px; bottom: 32px;
    display: flex; align-items: center; gap: 8px;
    font-size: 17px;
    color: var(--green);
  }
  .hours svg { width: 16px; height: 16px; }
</style>
</head>
<body>

<section class="card card--front" aria-label="Card front">
  <div class="brand">
    <span class="brand__mark"></span>
    <span class="brand__name">Maple Hollow Veterinary Hospital</span>
  </div>
  <div class="color-bar">
    <span class="green"></span><span class="brown"></span><span class="slate"></span><span class="orange"></span>
  </div>
</section>

<section class="card card--back" aria-label="Card back">
  <div class="mini-brand">
    <span class="mini-brand__mark"></span>
    <span class="mini-brand__name">Maple Hollow</span>
  </div>

  <ul class="doctors">
    <li>Owen Farrow</li>
    <li>Miriam Dale</li>
    <li>Clara Whitby</li>
    <li>Nora Pellham</li>
    <li>Lena Marsh</li>
    <li class="credential">DVM</li>
  </ul>

  <div class="divider"></div>

  <ul class="contact">
    <li><svg viewBox="0 0 12 12"><path d="M6 0a4 4 0 0 0-4 4c0 3 4 8 4 8s4-5 4-8a4 4 0 0 0-4-4zm0 5.5A1.5 1.5 0 1 1 6 2.5a1.5 1.5 0 0 1 0 3z"/></svg>4820 Cedar Bend Road</li>
    <li class="cont">Fairhaven, TX 75310</li>
    <li><svg viewBox="0 0 12 12"><path d="M2.5 0.5 4.5 3 3.4 4.6c.8 1.6 2.2 3 3.9 3.9L8.9 7.4 11.5 9.4 10.3 11.4C5.5 11 1 6.5.6 1.7z"/></svg>(555) 214-6080</li>
    <li><svg viewBox="0 0 12 12"><rect x="3" y="0.5" width="6" height="3.5"/><rect x="0.5" y="4.5" width="11" height="5" rx="1"/><rect x="3" y="8" width="6" height="3.5"/></svg>(555) 214-6091</li>
    <li><svg viewBox="0 0 12 12"><path d="M0.5 2h11v8h-11z M0.5 2 6 6.5 11.5 2" fill="none" stroke="var(--brown)" stroke-width="1.4"/></svg>info@tqrn.net</li>
    <li><svg viewBox="0 0 12 12"><circle cx="6" cy="6" r="5" fill="none" stroke="var(--brown)" stroke-width="1.3"/><path d="M1 6h10M6 1c-2.5 3-2.5 7 0 10M6 1c2.5 3 2.5 7 0 10" fill="none" stroke="var(--brown)" stroke-width="1"/></svg>www.tqrn.net</li>
  </ul>

  <p class="hours">
    <svg viewBox="0 0 16 16"><circle cx="8" cy="8" r="6.5" fill="none" stroke="var(--green)" stroke-width="1.8"/><path d="M8 4v4.3h3" fill="none" stroke="var(--green)" stroke-width="1.8"/></svg>
    Mon-Friday 7-6, Sat 8-12, Sun Closed
  </p>
</section>

</body>
</html>
```